Business Card, Stationery
Tax & Accounting Services
Professional
Lirena Vostrup EA
Tax Professional / Enrolled Agent
417 W Callory Avenue
Suite B
Bronx NY 10458
lvfiscalhub@quorvane.com
lvfiscalhub.com
Services:
Individual Tax Preparation
Business Tax Preparation
Tax Planning
DTB & State Tax Problems
Accounting
Payroll
Sales Tax
New Business Formation
Quickbooks Setup

```html
<!DOCTYPE html>
<html lang="en">
<head>
<meta charset="utf-8">
<title>LV Fiscal Hub Inc. — Stationery</title>
<link href="https://fonts.googleapis.com/css2?family=Montserrat:wght@600;700&family=Open+Sans:wght@400;600&display=swap" rel="stylesheet">
<style>
  :root{
    --backdrop:#2f2f31;
    --paper:#ffffff;
    --navy:#1d3c8a;
    --navy-deep:#132b66;
    --red:#c9252c;
    --red-deep:#98161c;
    --ink:#3a3f4a;
    --muted:#8a90a0;
    --label:#9a9aa0;
    --faint:rgba(29,60,138,.08);
  }
  *{box-sizing:border-box;margin:0;padding:0}
  html,body{width:1200px;height:338px;overflow:hidden}
  body{background:var(--backdrop);font-family:"Open Sans",Arial,sans-serif;position:relative}

  .sheet{position:absolute;background:var(--paper);overflow:hidden;box-shadow:0 2px 6px rgba(0,0,0,.35)}
  .item-label{position:absolute;font-size:4.5px;color:var(--label);white-space:nowrap}

  .brand{display:flex;align-items:center;gap:3px}
  .brand-dot{border-radius:50%;background:var(--navy);flex:none}
  .brand-name{font-family:"Montserrat",Arial,sans-serif;font-weight:700;color:var(--navy);white-space:nowrap}

  .watermark{position:absolute;font-family:"Montserrat",Arial,sans-serif;font-weight:700;color:var(--faint);white-space:nowrap;text-align:center}

  .band{position:absolute;left:0;bottom:0;width:100%}

  /* business cards */
  .card{width:63px;height:37px}
  .card-front{left:26px;top:113px}
  .card-back{left:26px;top:178px}
  .card .brand{position:absolute;left:6px;top:8px}
  .card .brand-dot{width:5px;height:5px}
  .card .brand-name{font-size:4px}
  .card-person{position:absolute;left:6px;top:17px;font-size:2.6px;color:var(--ink);line-height:1.35}
  .card-person b{font-weight:600;color:var(--navy)}
  .card-back .brand{left:50%;top:12px;transform:translateX(-50%)}

  /* letterheads */
  .letterhead{top:12px;width:226px;height:312px}
  .letterhead-1{left:132px}
  .letterhead-2{left:384px}
  .letterhead .brand{position:absolute;left:16px;top:14px}
  .letterhead .brand-dot{width:12px;height:12px}
  .letterhead .brand-name{font-size:7px}
  .lh-contact{position:absolute;right:14px;top:14px;font-size:3.4px;line-height:1.45;color:var(--muted);text-align:right}
  .letterhead .watermark{left:0;right:0;top:170px;font-size:22px}
  .lh-footer{position:absolute;left:0;right:0;bottom:14px;text-align:center;font-size:3.2px;color:var(--muted)}

  /* envelopes front */
  .envelope{left:629px;width:228px;height:108px}
  .envelope-1{top:41px}
  .envelope-2{top:173px}
  .envelope .brand{position:absolute;left:10px;top:10px}
  .envelope .brand-dot{width:9px;height:9px}
  .envelope .brand-name{font-size:5.5px}
  .env-return{position:absolute;left:10px;top:23px;font-size:3px;line-height:1.4;color:var(--muted)}
  .envelope .watermark{right:12px;top:50px;font-size:14px}

  /* envelope backs */
  .env-back{left:912px;width:205px;height:96px}
  .env-back-blue{top:12px;background:var(--navy)}
  .env-back-red{top:90px;background:var(--red)}
  .env-back-white{top:170px;background:var(--paper)}
  .env-back svg{position:absolute;inset:0;width:100%;height:100%}
  .env-back .brand{position:absolute;left:50%;top:22px;transform:translateX(-50%)}
  .env-back .brand-dot{width:6px;height:6px;background:#fff}
  .env-back .brand-name{font-size:4px;color:#fff}
  .env-back-white .brand-dot{background:var(--navy)}
  .env-back-white .brand-name{color:var(--navy)}
</style>
</head>
<body>

<!-- business cards -->
<div class="sheet card card-front">
  <div class="brand"><span class="brand-dot"></span><span class="brand-name">LV Fiscal Hub Inc.</span></div>
  <div class="card-person"><b>Lirena Vostrup EA</b><br>Tax Professional / Enrolled Agent<br>lvfiscalhub.com</div>
  <svg class="band" viewBox="0 0 100 6" preserveAspectRatio="none" height="3"><rect width="100" height="6" fill="#1d3c8a"/><polygon points="55,0 100,0 100,6 50,6" fill="#c9252c"/></svg>
</div>
<div class="item-label" style="left:26px;top:153px">Business Card Front</div>

<div class="sheet card card-back">
  <div class="brand"><span class="brand-dot"></span><span class="brand-name">LV Fiscal Hub Inc.</span></div>
  <svg class="band" viewBox="0 0 100 6" preserveAspectRatio="none" height="3"><rect width="100" height="6" fill="#1d3c8a"/><polygon points="55,0 100,0 100,6 50,6" fill="#c9252c"/></svg>
</div>
<div class="item-label" style="left:26px;top:218px">Business Card Back</div>

<!-- letterheads -->
<div class="sheet letterhead letterhead-1">
  <div class="brand"><span class="brand-dot"></span><span class="brand-name">LV Fiscal Hub Inc.</span></div>
  <div class="lh-contact">417 W Callory Avenue, Suite B<br>Bronx NY 10458<br>(718) 555-0143<br>lvfiscalhub@quorvane.com</div>
  <div class="watermark">LV Fiscal Hub</div>
  <div class="lh-footer">Individual &amp; Business Tax Preparation · Payroll · lvfiscalhub.com</div>
  <svg class="band" viewBox="0 0 100 4" preserveAspectRatio="none" height="6"><rect width="100" height="4" fill="#1d3c8a"/><polygon points="52,0 100,0 100,4 48,4" fill="#c9252c"/></svg>
</div>
<div class="item-label" style="left:210px;top:327px">Letterhead Version 1</div>

<div class="sheet letterhead letterhead-2">
  <div class="brand"><span class="brand-dot"></span><span class="brand-name">LV Fiscal Hub Inc.</span></div>
  <div class="watermark">LV Fiscal Hub</div>
  <div class="lh-footer">417 W Callory Avenue, Suite B, Bronx NY 10458 · lvfiscalhub@quorvane.com</div>
  <svg class="band" viewBox="0 0 100 4" preserveAspectRatio="none" height="6"><rect width="100" height="4" fill="#1d3c8a"/><polygon points="52,0 100,0 100,4 48,4" fill="#c9252c"/></svg>
</div>
<div class="item-label" style="left:462px;top:327px">Letterhead Version 2</div>

<!-- envelopes front -->
<div class="sheet envelope envelope-1">
  <div class="brand"><span class="brand-dot"></span><span class="brand-name">LV Fiscal Hub Inc.</span></div>
  <div class="env-return">417 W Callory Avenue, Suite B<br>Bronx NY 10458</div>
  <div class="watermark">LV Fiscal Hub</div>
  <svg class="band" viewBox="0 0 100 4" preserveAspectRatio="none" height="5"><rect width="100" height="4" fill="#1d3c8a"/><polygon points="52,0 100,0 100,4 48,4" fill="#c9252c"/></svg>
</div>
<div class="item-label" style="left:712px;top:152px">Envelope Front 1</div>

<div class="sheet envelope envelope-2">
  <div class="brand"><span class="brand-dot"></span><span class="brand-name">LV Fiscal Hub Inc.</span></div>
  <div class="env-return">417 W Callory Avenue, Suite B<br>Bronx NY 10458</div>
  <div class="watermark">LV Fiscal Hub</div>
  <svg class="band" viewBox="0 0 100 4" preserveAspectRatio="none" height="5"><rect width="100" height="4" fill="#1d3c8a"/><polygon points="52,0 100,0 100,4 48,4" fill="#c9252c"/></svg>
</div>
<div class="item-label" style="left:712px;top:284px">Envelope Front 2</div>

<!-- envelope backs -->
<div class="sheet env-back env-back-blue">
  <svg viewBox="0 0 100 48" preserveAspectRatio="none"><polygon points="0,0 100,0 100,8 50,26 0,8" fill="#132b66"/></svg>
  <div class="brand"><span class="brand-dot"></span><span class="brand-name">LV Fiscal Hub Inc.</span></div>
</div>
<div class="sheet env-back env-back-red">
  <svg viewBox="0 0 100 48" preserveAspectRatio="none"><polygon points="0,0 100,0 100,8 50,26 0,8" fill="#98161c"/></svg>
  <div class="brand"><span class="brand-dot"></span><span class="brand-name">LV Fiscal Hub Inc.</span></div>
</div>
<div class="sheet env-back env-back-white">
  <svg viewBox="0 0 100 48" preserveAspectRatio="none"><polygon points="0,0 100,0 100,8 50,26 0,8" fill="#1d3c8a"/><polyline points="0,8 50,26 100,8" fill="none" stroke="#c9252c" stroke-width="1"/></svg>
  <div class="brand"><span class="brand-dot"></span><span class="brand-name">LV Fiscal Hub Inc.</span></div>
</div>
<div class="item-label" style="left:992px;top:272px">Envelope Backs</div>

</body>
</html>
```